Letterhead for sustainable Last Mile Logistics needed

Dear all,

we are looking for a powerful design for our letterhead. We are a Berlin-based (Germany) logistics company which delivers parcel on the last mile in a sustainable way. Design should communicate: sustainability, integrity, one family, performance-focused, passionate for excellence and customer experience. Please find company logo attached.

Looking forward for

```html
<!DOCTYPE html>
<html lang="en">
<head>
<meta charset="utf-8">
<title>Leafway Logistics Letterhead</title>
<link rel="stylesheet" href="https://fonts.googleapis.com/css2?family=Arimo:wght@400;700&family=Questrial&display=swap">
<style>
  :root {
    --green-deep: #1b9a48;
    --green-lime: #9ecb3b;
    --ink: #555759;
    --ink-soft: #6a6c6e;
    --paper: #ffffff;
    --backdrop: #dedede;
    --rule: #8a8c8e;
  }
  * { margin: 0; padding: 0; box-sizing: border-box; }
  html, body {
    width: 1189px; height: 1200px; overflow: hidden;
    background: var(--backdrop);
  }
  .letterhead {
    position: absolute; left: 170px; top: 0;
    width: 848px; height: 1200px;
    background: var(--paper);
    font-family: "Arimo", Arial, sans-serif;
    color: var(--ink);
  }
  .header-band {
    position: absolute; left: 0; top: 0; width: 848px; height: 86px;
    background: linear-gradient(180deg, var(--green-deep) 0%, var(--green-deep) 45%, var(--green-lime) 100%);
  }
  .brand {
    position: absolute; left: 64px; top: 100px;
    display: flex; align-items: center; gap: 14px;
  }
  .brand-dot { width: 58px; height: 58px; border-radius: 50%; background: var(--green-deep); }
  .brand-name {
    font-family: "Arimo", Arial, sans-serif; font-weight: 700;
    font-size: 26px; color: var(--green-deep); letter-spacing: 0.5px;
  }
  .contact {
    position: absolute; left: 619px; top: 116px; height: 83px;
    border-left: 1px solid var(--rule);
    padding-left: 13px; font-size: 13px; line-height: 16.5px; color: var(--ink-soft);
    font-style: normal;
  }
  .contact-address { margin-bottom: 6px; }
  .contact-line { display: flex; align-items: center; gap: 8px; }
  .contact-line svg { width: 10px; height: 10px; flex: none; }
  .letter { position: absolute; left: 77px; top: 372px; width: 720px; }
  .salutation {
    font-family: "Questrial", "Century Gothic", sans-serif; font-weight: 700;
    font-size: 19.5px; color: var(--ink); margin-bottom: 34px; -webkit-text-stroke: 0.3px var(--ink);
  }
  .letter p {
    font-size: 13.85px; line-height: 17.4px; margin-bottom: 15.5px;
    color: var(--ink-soft); white-space: nowrap;
  }
  .closing {
    font-family: "Questrial", "Century Gothic", sans-serif; font-weight: 700;
    font-size: 10.5px; margin-top: 38px; color: var(--ink); -webkit-text-stroke: 0.2px var(--ink);
  }
  .signature {
    margin-top: 36px; width: 140px; height: 40px;
    background: linear-gradient(90deg, #e9e9ea, #f3f3f3);
    border-radius: 4px;
  }
</style>
</head>
<body>
  <main class="letterhead">
    <div class="header-band" role="img" aria-label="Green header band decoration"></div>

    <div class="brand">
      <span class="brand-dot"></span>
      <span class="brand-name">LEAFWAY LOGISTICS</span>
    </div>

    <address class="contact">
      <div class="contact-address">Your address, city<br>state, ZIP 0000</div>
      <div class="contact-line">
        <svg viewBox="0 0 10 10"><path fill="var(--green-deep)" d="M2,0.5 L3.6,2.6 L2.8,3.6 C3.4,5 4.8,6.5 6.3,7.2 L7.3,6.4 L9.5,8 L8.3,9.6 C4.5,9.2 0.8,5.5 0.4,1.7 Z"/></svg>
        <span>123-456-2100</span>
      </div>
      <div class="contact-line">
        <svg viewBox="0 0 10 10"><rect x="0.5" y="2" width="9" height="6.5" fill="var(--green-deep)"/><path d="M0.8,2.3 L5,5.8 L9.2,2.3" stroke="#fff" stroke-width="0.9" fill="none"/></svg>
        <span>youremail@leafwaymail.com</span>
      </div>
      <div class="contact-line">
        <svg viewBox="0 0 10 10"><circle cx="5" cy="5" r="4.5" fill="var(--green-deep)"/><path d="M0.5,5 H9.5 M5,0.5 C3,3 3,7 5,9.5 M5,0.5 C7,3 7,7 5,9.5" stroke="#fff" stroke-width="0.7" fill="none"/></svg>
        <span>www.yourwebsite.com</span>
      </div>
    </address>

    <section class="letter">
      <h1 class="salutation">Dear Mr. Smith,</h1>
      <p>Lorem ipsum dolor sit amet, consectetuer adipiscing elit, sed diam nonmmy nibh euismod tincidunt ut laor<br>eet dolore magna aliquam erat volutpat. Ut wisi enim ad minim veniam, quis nostrud exerci tationmcorper<br>suscipit lobortis nisl ut aliquip ex ea commodo consequat. Duis autem vel eum iriure dolor in hendrerit in<br>vulputate velit esse molestie consequat, vel illum dolore eu feugiat</p>
      <p>Rorem ipsum dolor sit amet, consectetuer adipiscing elit, sed diam nonmmy nibh euismod tincidunt ut laor<br>eet dolore magna aliquam erat volutpat. Ut wisi enim ad minim veniam, quis nostrud exerci tationmcorper<br>suscipit lobortis nisl ut aliquip ex ea commodo consequat. Duis autem vel eum iriure dolor in hendrerit in<br>vulputate velit esse molest</p>
      <p>Dorem ipsum dolor sit amet, consectetuer adipiscing elit, sed diam nonmmy nibh euismod tincidunt ut laor<br>eet dolore magna aliquam erat volutpat. Ut wisi enim ad minim veniam, quis nostrud exerci tationmcorper<br>suscipit lobortis nisl ut aliquip ex ea commodo consequat. Duis autem vel eum iriure dolor in hendrerit in<br>suscipit lobortis nisl ut aliquip ex ea commodo consequat. Duis autem vel eum iriure dolor in hendrerit in<br>vulputate velit esse molestie consequat, vel illum</p>
      <p>Sorem ipsum dolor sit amet, consectetuer adipiscing elit, sed diam nonmmy nibh euismod tincidunt ut laor<br>eet dolore magna aliquam erat volutpat. Ut wisi enim ad minim veniam, quis nostrud exerci tationmcorper<br>suscipit lobortis nisl ut aliquip ex ea commodo consequat. Duis autem vel eum iriure dolor in</p>
      <div class="closing">Sincerely,</div>
      <div class="signature" role="img" aria-label="Handwritten signature of the sender"></div>
    </section>
  </main>
</body>
</html>
```